Legal Stationary

A full set of stationery is required
The image and logo, along with colour, are set and attached.
The style should be modern, clean, and corporate. Not just a basic template off the web.
In addition to the address/website/email/phone fields for DX and KWT number, with the text “the firm is authorised and regulated by the KWT”
All files in all formats will be needed to allow editing after. Initial setup of templates will be required, and details for 4 business cards will be supplied.
Target Market(s)
Consumers of legal services
Industry/Entity Type
Legal

```html
<!DOCTYPE html>
<html lang="en">
<head>
<meta charset="utf-8">
<title>Hale Law — Stationery Set</title>
<link href="https://fonts.googleapis.com/css2?family=Montserrat:wght@400;500;700&family=Open+Sans:wght@400;600&display=swap" rel="stylesheet">
<style>
  :root {
    --backdrop: #a3a3a3;
    --paper: #ffffff;
    --page: #f7f7f7;
    --brand: #2b3a94;
    --ink: #1b1b1b;
    --muted: #3d3d3d;
    --rule: #8a8a8a;
    --fade: #eef1ec;
  }
  * { box-sizing: border-box; margin: 0; padding: 0; }
  html, body { width: 1200px; height: 946px; overflow: hidden; }
  body {
    position: relative;
    background: var(--backdrop);
    font-family: "Montserrat", sans-serif;
    color: var(--ink);
  }
  .piece { position: absolute; background: var(--paper); }
  .wordmark {
    position: absolute;
    font-family: "Montserrat", sans-serif;
    font-weight: 500;
    color: var(--brand);
    letter-spacing: 0.02em;
    white-space: nowrap;
    line-height: 1;
  }

  /* Business card — front */
  .card { width: 316px; height: 180px; border-radius: 12px; }
  .card--front { left: 87px; top: 85px; }
  .card--front .wordmark { left: 32px; top: 62px; font-size: 44px; }
  .card__regulation {
    position: absolute; left: 0; right: 0; top: 157px;
    text-align: center; font-size: 8.5px; color: var(--muted);
  }

  /* Business card — back */
  .card--back { left: 87px; top: 290px; }
  .card--back .wordmark { left: 27px; top: 78px; font-size: 22px; }
  .card__divider {
    position: absolute; left: 168px; top: 41px; width: 1px; height: 98px;
    background: var(--brand);
  }
  .card__details { position: absolute; left: 181px; top: 38px; font-size: 8.6px; color: var(--muted); }
  .card__name { font-size: 13.5px; color: var(--brand); letter-spacing: 0.01em; }
  .card__name b { font-weight: 700; }
  .card__role { margin-top: 2px; }
  .card__address { margin-top: 9px; line-height: 13px; }
  .card__contacts { margin-top: 5px; line-height: 12.6px; list-style: none; }
  .card__contacts li { display: flex; align-items: center; gap: 4px; }
  .card__contacts svg { width: 7px; height: 7px; fill: var(--brand); }

  /* Letterhead */
  .letterhead { left: 429px; top: 89px; width: 269px; height: 348px; font-family: "Open Sans", sans-serif; }
  .letterhead .wordmark { left: 25px; top: 27px; font-size: 21px; }
  .letterhead__contact {
    position: absolute; left: 180px; top: 11px; padding-left: 4px;
    border-left: 0.6px solid var(--brand);
    font-size: 4.6px; line-height: 6.6px; color: var(--muted);
  }
  .letterhead__contact p + p { margin-top: 2px; }
  .letterhead__contact b { color: var(--brand); }
  .letterhead__salutation { position: absolute; left: 25px; top: 93px; font-size: 6.8px; font-weight: 600; }
  .letterhead__role { font-size: 5px; font-weight: 400; margin-top: 1px; }
  .letterhead__date { position: absolute; right: 25px; top: 104px; font-size: 4px; }
  .letterhead__body {
    position: absolute; left: 25px; top: 120px; width: 220px;
    font-size: 3.85px; line-height: 6.1px; text-align: justify; color: var(--muted);
  }
  .letterhead__body p + p { margin-top: 6px; }
  .letterhead__signature {
    position: absolute; left: 25px; top: 275px; width: 76px; height: 14px;
    background: linear-gradient(90deg, #d9d9d9, #ececec);
  }
  .letterhead__signoff { position: absolute; left: 25px; top: 299px; font-size: 6.4px; font-weight: 600; }

  /* Envelopes */
  .envelope--back { left: 724px; top: 89px; width: 399px; height: 172px; }
  .envelope--back .wordmark { left: 19px; top: 15px; font-size: 22px; }
  .envelope__divider { position: absolute; left: 151px; top: 13px; width: 1px; height: 28px; background: var(--brand); }
  .envelope__address { position: absolute; left: 157px; top: 19px; font-size: 6.4px; line-height: 8px; color: var(--muted); }
  .envelope--front { left: 719px; top: 290px; width: 401px; height: 176px; }
  .envelope__flap { position: absolute; left: 0; top: 0; width: 401px; height: 70px; }
  .envelope--front .wordmark { left: 106px; top: 14px; font-size: 33px; }

  /* Notebook cover */
  .notebook-cover { left: 192px; top: 525px; width: 248px; height: 354px; }
  .notebook-cover .wordmark { left: 25px; top: 160px; font-size: 34px; }

  /* Open notebook */
  .notebook-spread { left: 516px; top: 528px; width: 496px; height: 350px; background: var(--page); }
  .notebook-spread__gutter { position: absolute; left: 248px; top: 0; width: 2px; height: 100%; background: #d6d6d6; }
  .notebook-page { position: absolute; top: 0; width: 246px; height: 100%; }
  .notebook-page--left { left: 0; }
  .notebook-page--right { left: 251px; }
  .notebook-page .wordmark { left: 11px; top: 20px; font-size: 19px; }
  .notebook-page__date { position: absolute; top: 27px; font-size: 8px; color: var(--muted); }
  .notebook-page--left .notebook-page__date { left: 170px; }
  .notebook-page--right .notebook-page__date { left: 170px; }
  .notebook-page__art { position: absolute; left: 13px; top: 104px; width: 214px; height: 121px; background: var(--fade); border-radius: 4px; }
  .notebook-page__lines {
    position: absolute; left: 11px; top: 59px; width: 223px; height: 280px;
    background: repeating-linear-gradient(to bottom, transparent 0 13px, var(--rule) 13px 13.7px);
  }
</style>
</head>
<body>

  <section class="piece card card--front" aria-label="Business card front">
    <span class="wordmark">HALE LAW</span>
    <p class="card__regulation">the firm is authorised and regulated by the KWT</p>
  </section>

  <section class="piece card card--back" aria-label="Business card back">
    <span class="wordmark">HALE LAW</span>
    <span class="card__divider"></span>
    <div class="card__details">
      <p class="card__name"><b>DANIEL</b> REED</p>
      <p class="card__role">Managing Director</p>
      <p class="card__address">Your address, City<br>State, Zip 1234</p>
      <ul class="card__contacts">
        <li><svg viewBox="0 0 10 10"><path d="M1 4c0-2 2-3 4-3s4 1 4 3H7V3H3v1zM2 5h6l1 4H1z"/></svg>123 456 789</li>
        <li><svg viewBox="0 0 10 10"><path d="M0 2h10v1L5 6 0 3zM0 4l5 3 5-3v4H0z"/></svg>info@halelaw.com</li>
        <li><svg viewBox="0 0 10 10"><circle cx="5" cy="5" r="4.5"/></svg>www.halelaw.com</li>
      </ul>
    </div>
  </section>

  <section class="piece letterhead" aria-label="Letterhead">
    <span class="wordmark">HALE LAW</span>
    <div class="letterhead__contact">
      <p>Your address, City<br>State, Zip 1234</p>
      <p>123 456 789<br>info@halelaw.com<br>www.halelaw.com</p>
      <p><b>DX :</b> 123 456 789<br><b>KWT :</b> 123 456 789</p>
    </div>
    <div class="letterhead__salutation">Dear .Mrs Anna Clarke<p class="letterhead__role">Owner/ceo</p></div>
    <p class="letterhead__date">Date: 17-March-2025</p>
    <div class="letterhead__body">
      <p>Lorem ipsum dolor sit amet, consectetur adipiscing elit. Mauris imperdiet ultricies nisi at varius. Ut euismod molestie lorem id maximus. Interdum et malesuada fames ac ante ipsum primis in faucibus. Sed sed enim urna. Mauris non elit quis nulla tincidunt maximus in a quam. Maecenas quis tellus ut eros auctor rhoncus non sed dui. Pellentesque habitant morbi tristique senectus et netus et malesuada fames ac turpis egestas.</p>
      <p>Sed imperdiet vehicula ligula. Proin sodales faucibus tortor sit amet fermentum. Donec varius massa vitae porta pharetra. Curabitur nec velit id ex pharetra ornare nec vel orci. Nam tristique diam sed ligula vehicula bibendum.</p>
      <p>Nunc semper nisl eget dolor tempus tincidunt. Orci varius natoque penatibus et magnis dis parturient montes, nascetur ridiculus mus. Mauris at tristique quam, sed accumsan risus. Proin odio libero, dignissim a neque vitae, sodales tempor nisl. Nulla commodo lobortis purus.</p>
      <p>Cras sed tortor faucibus, pellentesque lacus at, faucibus lacus. Sed ac lobortis diam. Duis eget sapien consequat quam scelerisque egestas in sit amet nunc. Praesent posuere, mi eu pulvinar vestibulum, mauris mi laoreet dui, ut lacinia neque elit sit amet metus.</p>
      <p>Vivamus vel vehicula erat, vitae suscipit erat. Nullam lacinia, sem ac euismod cursus, justo nisi ultrices nunc, sed mollis eros diam quis lectus.</p>
    </div>
    <div class="letterhead__signature" role="img" aria-label="Handwritten signature of Mrs Anna Clarke"></div>
    <div class="letterhead__signoff">Mrs Anna Clarke<p class="letterhead__role">Owner/ceo</p></div>
  </section>

  <section class="piece envelope--back" aria-label="Envelope back">
    <span class="wordmark">HALE LAW</span>
    <span class="envelope__divider"></span>
    <p class="envelope__address">Your address, City<br>State, Zip 1234</p>
  </section>

  <section class="piece envelope--front" aria-label="Envelope front">
    <svg class="envelope__flap" viewBox="0 0 401 70" aria-hidden="true">
      <path d="M0 0 Q8 40 22 54 Q30 63 48 63 H360 Q376 63 384 52 Q396 36 401 0" fill="none" stroke="#d2d2d2" stroke-width="1"/>
    </svg>
    <span class="wordmark">HALE LAW</span>
  </section>

  <section class="piece notebook-cover" aria-label="Notebook cover">
    <span class="wordmark">HALE LAW</span>
  </section>

  <section class="piece notebook-spread" aria-label="Open notebook pages">
    <div class="notebook-page notebook-page--left">
      <span class="wordmark">HALE LAW</span>
      <p class="notebook-page__date">Date......./....../.......</p>
      <div class="notebook-page__art" role="img" aria-label="Faint background illustration"></div>
      <div class="notebook-page__lines"></div>
    </div>
    <span class="notebook-spread__gutter"></span>
    <div class="notebook-page notebook-page--right">
      <span class="wordmark">HALE LAW</span>
      <p class="notebook-page__date">Date......./....../.......</p>
      <div class="notebook-page__art" role="img" aria-label="Faint background illustration"></div>
      <div class="notebook-page__lines"></div>
    </div>
  </section>

</body>
</html>
```